Trade show Banner to be displayed on vertical stand

We are an IT company that specializes in working with Manufacturing companies and manufacturing plants. We need two banners designed for a manufacturing trade show. The design needs to be designed using the supplied template file. Also the design needs to communicate graphically that we specialize in working with manufacturing plants. Also they should communicate that out services include: IT Services, Network, Voice, Data

Target Market(s)

Manufacturing companies

Industry/Entity Type

Manufacturing

Requirements
Must have
• Clear message, clear graphic message. Must be designed with included templates
Nice to have
• Company colors need to be used, but additional colors can be used

```html
<!DOCTYPE html>
<html lang="en">
<head>
<meta charset="utf-8">
<title>Gridline Works – Trade Show Banner</title>
<link rel="stylesheet" href="https://fonts.googleapis.com/css2?family=Saira+Semi+Condensed:wght@500;700&display=swap">
<style>
  :root {
    --brand-blue: #2a86cb;
    --ink: #1c1c20;
    --stage: #ecebe8;
    --banner-top: #eef0f6;
    --banner-bottom: #d9dded;
    --pattern-light: #d7e6f4;
    --pattern-deep: #8fbfe6;
  }
  * { margin: 0; padding: 0; box-sizing: border-box; }
  html, body {
    width: 1200px;
    height: 2161px;
    overflow: hidden;
    background: var(--stage);
  }
  .canvas {
    position: relative;
    width: 1200px;
    height: 2161px;
  }
  .banner {
    position: absolute;
    left: 225px;
    top: 88px;
    width: 749px;
    height: 1984px;
    background: linear-gradient(180deg, var(--banner-top) 0%, var(--banner-bottom) 100%);
    overflow: hidden;
  }
  .banner-art {
    position: absolute;
    inset: 0;
    width: 100%;
    height: 100%;
  }
  .arc { fill: none; stroke: var(--brand-blue); }
  .arc-thick { stroke-width: 9; }
  .arc-thin { stroke-width: 3; }
  .wordmark {
    font-family: "Saira Semi Condensed", sans-serif;
    font-weight: 700;
    font-size: 82px;
    fill: var(--brand-blue);
  }
  .wordmark-second { letter-spacing: 14px; }
  .brand-dot { fill: var(--brand-blue); }

  .services {
    list-style: none;
    position: absolute;
    left: 0;
    top: 0;
    width: 100%;
  }
  .service {
    position: absolute;
    left: 0;
    height: 70px;
    display: flex;
    align-items: center;
    font-family: "Saira Semi Condensed", sans-serif;
    font-weight: 500;
    font-size: 58px;
    color: var(--ink);
  }
  .service-rule {
    width: 45px;
    height: 3px;
    background: var(--brand-blue);
  }
  .service-icon {
    width: 44px;
    height: 44px;
    margin: 0 32px 0 18px;
    flex: none;
  }
  .service-icon * { stroke: var(--brand-blue); fill: none; stroke-width: 3; }
  .service-icon .solid { fill: var(--brand-blue); stroke: none; }
  .service-it { top: 1000px; }
  .service-network { top: 1101px; }
  .service-voice { top: 1216px; }
  .service-data { top: 1325px; }
</style>
</head>
<body>
<main class="canvas">
  <section class="banner">
    <svg class="banner-art" viewBox="0 0 468 1240" preserveAspectRatio="none">
      <defs>
        <linearGradient id="pattern-tone" x1="0" y1="0" x2="1" y2="1">
          <stop offset="0" stop-color="var(--pattern-deep)"/>
          <stop offset="1" stop-color="var(--pattern-light)"/>
        </linearGradient>
      </defs>

      <path class="pattern-area" role="img" aria-label="Blue circuit-style maze pattern in the top corner"
            fill="url(#pattern-tone)"
            d="M0 0 H468 V30 A700 700 0 0 0 0 318 Z"/>
      <path class="arc arc-thick" d="M0 318 A700 700 0 0 1 468 30"/>
      <path class="arc arc-thin" d="M0 300 A710 710 0 0 1 468 14"/>

      <path class="pattern-area" role="img" aria-label="Blue circuit-style maze pattern in the bottom corner"
            fill="url(#pattern-tone)"
            d="M0 934 A640 640 0 0 1 468 1212 V1240 H0 Z"/>
      <path class="arc arc-thick" d="M0 934 A640 640 0 0 1 468 1212"/>
      <path class="arc arc-thin" d="M0 918 A650 650 0 0 1 468 1194"/>

      <g class="brand">
        <circle class="brand-dot" cx="372" cy="782" r="62"/>
        <text class="wordmark" transform="translate(374 660) rotate(-90)">gridline</text>
        <text class="wordmark wordmark-second" transform="translate(448 660) rotate(-90)">works</text>
      </g>
    </svg>

    <ul class="services">
      <li class="service service-it">
        <span class="service-rule"></span>
        <svg class="service-icon" viewBox="0 0 44 44"><path class="solid" d="M6 8 L32 4 V38 L6 42 Z"/><path d="M32 4 H38 V38 H32"/></svg>
        IT Services
      </li>
      <li class="service service-network">
        <span class="service-rule"></span>
        <svg class="service-icon" viewBox="0 0 44 44"><path d="M22 22 L8 10 M22 22 L36 10 M22 22 L38 26 M22 22 L12 36 M22 22 L28 38"/><circle class="solid" cx="22" cy="22" r="7"/><circle class="solid" cx="8" cy="10" r="4"/><circle class="solid" cx="36" cy="10" r="4"/><circle class="solid" cx="38" cy="26" r="4"/><circle class="solid" cx="12" cy="36" r="4"/><circle class="solid" cx="28" cy="38" r="4"/></svg>
        Network
      </li>
      <li class="service service-voice">
        <span class="service-rule"></span>
        <svg class="service-icon" viewBox="0 0 44 44"><rect class="solid" x="16" y="2" width="12" height="24" rx="6"/><path d="M10 20 A12 12 0 0 0 34 20 M22 32 V40 M14 41 H30"/></svg>
        Voice
      </li>
      <li class="service service-data">
        <span class="service-rule"></span>
        <svg class="service-icon" viewBox="0 0 44 44"><rect x="6" y="3" width="32" height="10" rx="5"/><rect x="6" y="17" width="32" height="10" rx="5"/><rect x="6" y="31" width="32" height="10" rx="5"/><path d="M12 8 H28 M12 22 H28 M12 36 H28"/></svg>
        Data
      </li>
    </ul>
  </section>
</main>
</body>
</html>
```